Talents and colours poster for home office

The objective is to illustrate/communicate and remember 5 talents and 4 colours of the personality.

The infographic will be hanged on the wall of an home office. It need to be simple and clear. Illustrations and pictograms can be used. It can be artistic.

Here's the content:

5 talents,scaling in priority from #1 to #5
Ideation / creativity
Winning other over / charisma
Adaptability
Positivity
Empathy

In the files there is a description of what those mean.

You have to include 4 colours, scaling in priority from #1 to #4
Yellow
Green
Red
Blue

I made a sketch just for fun... and to show why I need professionnal skills :)

THX

Industry/Entity Type

Office

Requirements
Should not have
• offensive materials

```html
<!DOCTYPE html>
<html lang="en">
<head>
<meta charset="utf-8">
<title>Talents Poster</title>
<link rel="stylesheet" href="https://fonts.googleapis.com/css2?family=Oswald:wght@500;600&display=swap">
<style>
  :root {
    --frame-black: #111111;
    --frame-white: #ffffff;
    --paint-orange: #f07a22;
    --paint-red: #d8332c;
    --paint-yellow: #f4d21f;
    --paint-blue: #3b5fb0;
    --paint-purple: #7a3f9a;
    --paint-green: #3f9a45;
    --panel-fill: rgba(255, 255, 255, 0.62);
    --panel-shadow: rgba(20, 20, 30, 0.75);
    --talent-yellow: #f5e634;
    --talent-yellow-edge: #c9b91c;
    --talent-green: #8cc540;
    --talent-green-edge: #5f8f27;
    --talent-red: #e63a2b;
    --talent-red-edge: #a7231a;
    --talent-navy: #2f4a8f;
    --talent-navy-edge: #1d2f5e;
    --talent-sky: #7095cb;
    --talent-sky-edge: #4d6ea3;
    --ink-dark: #1a1a1a;
    --ink-light: #ffffff;
  }
  html, body {
    margin: 0;
    padding: 0;
    overflow: hidden;
    background: #ffffff;
  }
  .poster {
    position: relative;
    width: 932px;
    height: 1200px;
    background: var(--frame-black);
    overflow: hidden;
  }
  .frame-line {
    position: absolute;
    inset: 16px;
    border: 5px solid var(--frame-white);
  }
  .paint-field {
    position: absolute;
    left: 35px;
    top: 35px;
    width: 862px;
    height: 1130px;
    background:
      radial-gradient(circle at 50% 45%, rgba(255,255,255,0.9) 0%, rgba(255,255,255,0.55) 35%, rgba(255,255,255,0) 60%),
      linear-gradient(100deg, var(--paint-orange) 0%, var(--paint-red) 14%, var(--paint-orange) 24%, rgba(255,255,255,0.6) 45%, rgba(255,255,255,0.6) 58%, var(--paint-purple) 78%, var(--paint-blue) 90%, var(--paint-orange) 100%),
      linear-gradient(180deg, var(--paint-yellow) 0%, var(--paint-green) 100%);
    background-blend-mode: normal, normal, multiply;
  }
  .talent-panel {
    position: absolute;
    left: 117px;
    top: 173px;
    width: 703px;
    height: 869px;
    background: var(--panel-fill);
    border-radius: 14px;
    box-shadow: 10px 10px 0 var(--panel-shadow);
  }
  .talent-list {
    position: absolute;
    left: 203px;
    top: 235px;
    width: 539px;
    margin: 0;
    padding: 0;
    list-style: none;
  }
  .talent {
    height: 116px;
    margin-bottom: 40px;
    border-radius: 12px;
    display: flex;
    align-items: center;
    justify-content: center;
    font-family: "Oswald", sans-serif;
    font-weight: 600;
    font-size: 30px;
    letter-spacing: 0.2px;
    text-transform: uppercase;
    background-image: linear-gradient(180deg, rgba(255,255,255,0.12) 0%, rgba(255,255,255,0.12) 50%, rgba(0,0,0,0.04) 50%, rgba(0,0,0,0.04) 100%);
  }
  .talent--yellow { background-color: var(--talent-yellow); color: var(--ink-dark); box-shadow: 0 8px 0 var(--talent-yellow-edge), 0 10px 4px rgba(0,0,0,0.35); }
  .talent--green  { background-color: var(--talent-green);  color: var(--ink-dark); box-shadow: 0 8px 0 var(--talent-green-edge), 0 10px 4px rgba(0,0,0,0.35); }
  .talent--red    { background-color: var(--talent-red);    color: var(--ink-light); box-shadow: 0 8px 0 var(--talent-red-edge), 0 10px 4px rgba(0,0,0,0.35); }
  .talent--navy   { background-color: var(--talent-navy);   color: var(--ink-light); box-shadow: 0 8px 0 var(--talent-navy-edge), 0 10px 4px rgba(0,0,0,0.35); }
  .talent--sky    { background-color: var(--talent-sky);    color: var(--ink-light); box-shadow: 0 8px 0 var(--talent-sky-edge), 0 10px 4px rgba(0,0,0,0.35); }
</style>
</head>
<body>
  <main class="poster">
    <div class="frame-line"></div>
    <div class="paint-field" role="img" aria-label="Colourful paint splatter and brush streak artwork in orange, red, yellow, green, purple and blue"></div>
    <div class="talent-panel"></div>
    <ol class="talent-list">
      <li class="talent talent--yellow">Ideation / Creativity</li>
      <li class="talent talent--green">Winning Other Over / Charisma</li>
      <li class="talent talent--red">Adaptability</li>
      <li class="talent talent--navy">Positivity</li>
      <li class="talent talent--sky">Empathy</li>
    </ol>
  </main>
</body>
</html>
```